Mossy Den Pet Supply

Thank you for your interest in this design contest. We are always welcome to questions and are looking forward to seeing what you can come up with.

We work on a Bootstrap platform with our custom built CMS. We require all designs to be sized accordingly with the bootstrap grid system found here: http://fernlattice.com/css/#grid

At the start of a competition, we are looking for general Home Page Design concepts and an example product grid page.

Homepage: Slide Show/Featured Products/Specials

example website as a reference:https://www.mintcollarworks.com/

Store Product Grid: Show a grid of product thumbnails. Included elements are thumbnail and price. Also included are filters (sort by, show by grid/list).

No photos at this time but Logo is attached. Looking for good quality photo's around the web. Please read the attached creative brief in depth to get an idea f what the client is looking for. Thanks!

```html
<!DOCTYPE html>
<html lang="en">
<head>
<meta charset="utf-8">
<title>Mossy Den Pet Supply</title>
<link href="https://fonts.googleapis.com/css2?family=PT+Sans:ital,wght@0,400;0,700;1,400&family=PT+Sans+Narrow:wght@400;700&family=PT+Serif:ital@1&display=swap" rel="stylesheet">
<style>
:root{
  --green:#7fbf2a;
  --green-light:#a6d64a;
  --green-dark:#4f8a16;
  --orange:#f7a21b;
  --yellow:#fbb91f;
  --ink:#2b2b2b;
  --grey:#777;
  --line:#d8d8d8;
  --footer:#161616;
  --footer-text:#9a9a9a;
}
*{margin:0;padding:0;box-sizing:border-box}
html,body{width:757px;height:1200px;overflow:hidden;background:#fff}
body{font-family:"PT Sans",Arial,sans-serif;color:var(--ink);position:relative}
.abs{position:absolute}
.narrow{font-family:"PT Sans Narrow","Arial Narrow",sans-serif;font-weight:700}

/* header */
.topbar{left:0;top:0;width:757px;height:27px;background:linear-gradient(#a9d755,#8cc63a)}
.header{left:0;top:27px;width:757px;height:61px;background:linear-gradient(#f7f7f7,#ececec);border-bottom:1px solid #e0e0e0}
.logo-box{left:100px;top:0;width:85px;height:82px;background:#fff;border-bottom:3px solid var(--orange);border-radius:0 0 4px 4px;box-shadow:0 1px 3px rgba(0,0,0,.2);display:flex;flex-direction:column;align-items:center;justify-content:center;text-align:center}
.logo-mark{width:14px;height:14px;background:var(--green);border-radius:50%;margin-bottom:5px}
.logo-name{font-family:"PT Sans Narrow",sans-serif;font-weight:700;font-size:12px;line-height:12px;color:var(--ink);text-transform:uppercase}
.util-links{left:210px;top:10px;display:flex;gap:15px;font-family:"PT Sans Narrow",sans-serif;font-size:6.5px;color:#fff;font-weight:700;text-transform:uppercase;white-space:nowrap}
.account-links{left:452px;top:9px;display:flex;gap:7px;font-size:6.5px;color:#2f4a10;white-space:nowrap}
.bag{left:570px;top:6px;width:62px;height:14px;background:#3f6d12;border-radius:8px;color:#fff;font-size:7.5px;font-weight:700;text-align:center;line-height:14px;font-family:"PT Sans Narrow",sans-serif;white-space:nowrap}
.bag-tab{left:632px;top:0;width:25px;height:33px}
.bag-count{left:648px;top:9px;font-size:8px;line-height:8px;color:var(--orange)}
.main-nav{left:209px;top:54px;display:flex;gap:12px;font-size:9.5px;color:#333;text-transform:uppercase;white-space:nowrap}
.main-nav .current{color:var(--green);border-bottom:2px solid var(--green);padding-bottom:2px}
.search{left:546px;top:50px;width:94px;height:17px;background:#fff;border:1px solid #ddd;font-size:6.5px;color:#aaa;padding:4px 5px}
.search-btn{left:640px;top:50px;width:17px;height:17px;background:var(--orange)}

/* hero */
.hero{left:0;top:88px;width:757px;height:188px;background:linear-gradient(180deg,#8cc6e8 0%,#c9e3f2 45%,#e6f1f6 70%,#6fae2a 88%,#3f8a16 100%)}
.hero-title{right:118px;top:100px;text-align:right;line-height:26px}
.hero-title .l1{font-size:26px;color:var(--green);margin-right:44px}
.hero-title .l2{font-size:26px;color:#2b2b2b}
.dots{left:107px;top:264px;display:flex;gap:3px}
.dots span{width:7px;height:7px;border-radius:50%;background:#e8e8e8}
.dots .on{background:var(--orange)}

/* promo tiles */
.tile{top:305px;width:131px;height:87px;border:1px solid var(--line);padding:3px;background:#fff}
.tile-photo{width:100%;height:100%;position:relative}
.tile-label{position:absolute;left:4px;bottom:23px;color:#fff;font-size:21px;line-height:22px;text-transform:uppercase;text-shadow:0 1px 3px rgba(0,0,0,.6);white-space:nowrap}
.btn{display:inline-block;background:linear-gradient(#78b62a,#4b8a14);color:#fff;font-family:"PT Sans Narrow",sans-serif;font-weight:700;font-size:8px;text-transform:uppercase;border:1px solid #3c7010;border-radius:2px;text-align:center}
.tile .btn{position:absolute;left:6px;bottom:5px;width:52px;height:13px;line-height:11px}

/* featured */
.section-title{font-size:14px;color:var(--green);text-transform:uppercase}
.rule-dotted{left:101px;top:440px;width:556px;border-top:1px dashed #c8c8c8}
.product{top:453px;width:133px;height:149px;border:1px solid var(--line);padding:3px;background:#fff}
.product-photo{height:79px}
.product-row{display:flex;justify-content:space-between;align-items:baseline;margin-top:3px;padding:0 2px;white-space:nowrap}
.price{color:var(--orange);font-size:14px}
.product-name{font-size:12px;text-transform:uppercase;color:#222}
.product-desc{font-size:6.4px;line-height:9px;color:#555;padding:0 3px;margin-top:4px}
.product .btn{margin:6px 0 0 3px;width:50px;height:13px;line-height:11px}

/* galleries */
.gallery-band{left:0;top:630px;width:757px;height:171px;background:var(--yellow)}
.band-title{font-size:15px;color:#222;text-transform:uppercase}
.thumb{border:2px solid #fff}
.video{left:525px;top:646px;width:132px;height:136px;border:3px solid #fff;background:linear-gradient(160deg,#5d6b3a,#8a8f64 50%,#c7c3b0)}
.play{left:569px;top:695px;width:43px;height:43px;border-radius:50%;background:rgba(255,255,255,.85)}

/* blog & news */
.col-title{font-size:15px;color:#222;font-weight:400}
.col-rule{border-top:1px solid #cfcfcf}
.arrows{display:flex;gap:3px}
.arrows span{width:10px;height:9px;background:#222;display:flex;align-items:center;justify-content:center}
.avatar{width:31px;height:31px;border-radius:50%;border:2px solid #e6e6e6;background:radial-gradient(circle,#e9c9a8,#b98a62)}
.blog-text{font-family:"PT Serif",Georgia,serif;font-style:italic;font-size:7.6px;line-height:12px;color:#777;width:210px}
.blog-name{font-family:"PT Serif",Georgia,serif;font-size:7.6px;color:var(--green-dark);margin-top:6px}
.date{width:26px;text-align:center}
.date-box{background:var(--yellow);height:27px;padding-top:2px}
.date-day{font-size:13px;line-height:12px;color:#222}
.date-mon{font-size:6px;color:#222}
.date-year{font-size:9px;color:var(--orange);font-weight:700}
.news-text{font-size:7.2px;line-height:10px;color:#555;width:214px}

/* footer */
.footer{left:0;top:1006px;width:757px;height:194px;background:linear-gradient(#1b1b1b,#101010)}
.foot-title{font-size:9.5px;color:var(--green);font-weight:400}
.foot-list{font-size:6.2px;line-height:11.5px;color:#ccc;list-style:none}
.foot-contact{font-size:6.4px;line-height:11.5px;color:#bbb}
.foot-contact b{color:var(--green-light);font-weight:400}
.fb-dot{width:14px;height:14px;border-radius:50%;background:#3b5a96}
.fb-text{font-size:6.1px;line-height:8px;color:#777;width:140px}
.foot-rule{left:101px;top:1137px;width:556px;border-top:1px solid #2e2e2e}
.follow{left:103px;top:1144px;display:flex;align-items:center;gap:3px;font-size:6.4px;color:#ccc}
.follow i{width:10px;height:10px;background:#4d7bc4;border-radius:1px;display:inline-block}
.copyright{right:100px;top:1143px;text-align:right;font-size:6.2px;line-height:9px;color:#888}
</style>
</head>
<body>

<header>
  <div class="abs topbar"></div>
  <div class="abs header"></div>
  <div class="abs logo-box">
    <div class="logo-mark"></div>
    <div class="logo-name">Mossy Den<br>Pet Supply</div>
  </div>
  <nav class="abs util-links"><span>Reservations</span><span>Event Calendar</span><span>Photo Galleries</span><span>Video Galleries</span></nav>
  <div class="abs account-links"><span>My Account</span><span>Login</span><span>Join Now</span></div>
  <div class="abs bag">My Shopping Bag</div>
  <svg class="abs bag-tab" viewBox="0 0 25 33" width="25" height="33">
    <path d="M0 0 H25 V24 L12.5 33 L0 24 Z" fill="#fff"/>
    <rect x="4" y="8" width="9" height="12" rx="1.5" fill="#f7a21b"/>
    <path d="M6 8 V6 a2.5 2.5 0 0 1 5 0 V8" fill="none" stroke="#f7a21b" stroke-width="1.2"/>
  </svg>
  <div class="abs bag-count">0</div>
  <nav class="abs main-nav narrow"><span class="current">Home</span><span>Dogs</span><span>Cats</span><span>Our Story</span><span>The Scoop</span><span>Find a Retailer</span><span>Retailers</span></nav>
  <div class="abs search">Search here...</div>
  <div class="abs search-btn">
    <svg width="17" height="17" viewBox="0 0 17 17"><circle cx="7.5" cy="7.5" r="3.2" fill="none" stroke="#5a3a00" stroke-width="1.5"/><line x1="10" y1="10" x2="13" y2="13" stroke="#5a3a00" stroke-width="2"/></svg>
  </div>
</header>

<section>
  <div class="abs hero" role="img" aria-label="Two children running on grass with a curly brown dog on a leash under a blue sky"></div>
  <div class="abs hero-title"><div class="l1">Redefining</div><div class="l2">pet services</div></div>
  <div class="abs dots"><span></span><span></span><span class="on"></span><span></span></div>
</section>

<section>
  <div class="abs tile" style="left:102px"><div class="tile-photo" role="img" aria-label="Woman greeting a dog at home" style="background:linear-gradient(135deg,#8a7a5a,#d9cfbd 60%,#a58c6a)"><div class="tile-label narrow">Reservations</div><span class="btn">Learn More</span></div></div>
  <div class="abs tile" style="left:243px"><div class="tile-photo" role="img" aria-label="Close view of a printed calendar" style="background:linear-gradient(135deg,#6f6f6f,#c4c4c4 60%,#8d8d8d)"><div class="tile-label narrow">Event<br>Calendar</div><span class="btn">Learn More</span></div></div>
  <div class="abs tile" style="left:384px"><div class="tile-photo" role="img" aria-label="Small dog being groomed" style="background:linear-gradient(135deg,#b07a45,#e3c6a0 60%,#9c6a3a)"><div class="tile-label narrow">Specials</div><span class="btn">Learn More</span></div></div>
  <div class="abs tile" style="left:525px"><div class="tile-photo" role="img" aria-label="Smiling woman outdoors with her dog" style="background:linear-gradient(135deg,#6c8a3a,#c9b48a 60%,#7a9a42)"><div class="tile-label narrow">Find a<br>Retailer</div><span class="btn">Learn More</span></div></div>
</section>

<section>
  <h2 class="abs section-title narrow" style="left:101px;top:421px">Featured Products</h2>
  <div class="abs rule-dotted"></div>

  <article class="abs product" style="left:101px">
    <div class="product-photo" role="img" aria-label="Beagle puppy sitting on a scale" style="background:linear-gradient(150deg,#b26d3c,#e7d8c4 55%,#8d8d8d)"></div>
    <div class="product-row narrow"><span class="price">$280</span><span class="product-name">Dog Toys</span></div>
    <p class="product-desc">Lorem Ipsum is simply dummy text of the printing and typesetting industry</p>
    <span class="btn">Order Now</span>
  </article>
  <article class="abs product" style="left:242px">
    <div class="product-photo" role="img" aria-label="Puppy resting on a bed" style="background:linear-gradient(150deg,#c9a170,#efe3cf 55%,#b89468)"></div>
    <div class="product-row narrow"><span class="price">$280</span><span class="product-name">Dog Beds</span></div>
    <p class="product-desc">Lorem Ipsum is simply dummy text of the printing and typesetting industry</p>
    <span class="btn">Order Now</span>
  </article>
  <article class="abs product" style="left:383px">
    <div class="product-photo" role="img" aria-label="Small dog among pink towels and flowers" style="background:linear-gradient(150deg,#e39ac7,#f6d7e8 55%,#d17fb0)"></div>
    <div class="product-row narrow"><span class="price">$280</span><span class="product-name">Dog Apparel</span></div>
    <p class="product-desc">Lorem Ipsum is simply dummy text of the printing and typesetting industry</p>
    <span class="btn">Order Now</span>
  </article>
  <article class="abs product" style="left:524px">
    <div class="product-photo" role="img" aria-label="Dog lying under a blue blanket" style="background:linear-gradient(150deg,#dfe8ee,#7aa3c4 55%,#3e6e9c)"></div>
    <div class="product-row narrow"><span class="price">$280</span><span class="product-name">Blankets</span></div>
    <p class="product-desc">Lorem Ipsum is simply dummy text of the printing and typesetting industry</p>
    <span class="btn">Order Now</span>
  </article>
</section>

<section>
  <div class="abs gallery-band"></div>
  <h2 class="abs band-title narrow" style="left:101px;top:642px">Our Photo Galleries</h2>
  <div class="abs thumb" role="img" aria-label="Puppy lying down" style="left:101px;top:668px;width:78px;height:51px;background:linear-gradient(135deg,#7a4a2a,#d9b89a)"></div>
  <div class="abs thumb" role="img" aria-label="Cat resting" style="left:189px;top:668px;width:78px;height:51px;background:linear-gradient(135deg,#d9a46a,#f1dcc0)"></div>
  <div class="abs thumb" role="img" aria-label="Pug on grass" style="left:277px;top:668px;width:78px;height:51px;background:linear-gradient(135deg,#6a9a3a,#d8c7a0)"></div>
  <div class="abs thumb" role="img" aria-label="Black and white puppy" style="left:101px;top:730px;width:78px;height:51px;background:linear-gradient(135deg,#f2f2f2,#2a2a2a)"></div>
  <div class="abs thumb" role="img" aria-label="Child hugging a dog" style="left:189px;top:730px;width:78px;height:51px;background:linear-gradient(135deg,#f4f4f4,#5c7fa8)"></div>
  <div class="abs thumb" role="img" aria-label="Golden retriever" style="left:277px;top:730px;width:78px;height:51px;background:linear-gradient(135deg,#5a3a1c,#d89b4a)"></div>

  <h2 class="abs band-title narrow" style="left:384px;top:642px">Video Galleries</h2>
  <div class="abs thumb" role="img" aria-label="Three dogs sitting together" style="left:384px;top:668px;width:62px;height:51px;background:linear-gradient(135deg,#e9e9e9,#9a7a52)"></div>
  <div class="abs thumb" role="img" aria-label="Woman training a dog" style="left:454px;top:668px;width:62px;height:51px;background:linear-gradient(135deg,#8aa45a,#5c4a3a)"></div>
  <div class="abs thumb" role="img" aria-label="Dog eating from a bowl" style="left:384px;top:730px;width:62px;height:51px;background:linear-gradient(135deg,#8a7a6a,#c9c0b0)"></div>
  <div class="abs thumb" role="img" aria-label="Dark dog portrait" style="left:454px;top:730px;width:62px;height:51px;background:linear-gradient(135deg,#2a1e1a,#7a4a3a)"></div>
  <div class="abs video" role="img" aria-label="Video still of a woman kneeling beside a small white dog"></div>
  <div class="abs play"><svg width="43" height="43" viewBox="0 0 43 43"><path d="M17 13 L30 21.5 L17 30 Z" fill="#222"/></svg></div>
</section>

<section>
  <h2 class="abs col-title" style="left:101px;top:825px">Recent Blog</h2>
  <div class="abs arrows" style="left:333px;top:833px"><span><svg width="5" height="5" viewBox="0 0 5 5"><path d="M4 0 L1 2.5 L4 5Z" fill="#fff"/></svg></span><span><svg width="5" height="5" viewBox="0 0 5 5"><path d="M1 0 L4 2.5 L1 5Z" fill="#fff"/></svg></span></div>
  <div class="abs col-rule" style="left:101px;top:846px;width:256px"></div>

  <div class="abs avatar" role="img" aria-label="Author portrait" style="left:104px;top:857px"></div>
  <div class="abs" style="left:143px;top:856px">
    <p class="blog-text">Lorem Ipsum is simply dummy text of the printing and type-setting industry. Lorem Ipsum has been the industry's standard dummy text ever since the 1500s,</p>
    <p class="blog-name">Lena Marwick</p>
  </div>
  <div class="abs avatar" role="img" aria-label="Author portrait" style="left:104px;top:917px"></div>
  <div class="abs" style="left:143px;top:916px">
    <p class="blog-text">Lorem Ipsum is simply dummy text of the printing and typeset-ting industry. Lorem Ipsum has been the industry's standard dummy text ever since the 1500s, when an unknown printer took a galley of type and scrambled it to make a type</p>
    <p class="blog-name">Tobin Hale</p>
  </div>

  <h2 class="abs col-title" style="left:403px;top:825px">Latest News</h2>
  <div class="abs arrows" style="left:635px;top:833px"><span><svg width="5" height="5" viewBox="0 0 5 5"><path d="M4 0 L1 2.5 L4 5Z" fill="#fff"/></svg></span><span><svg width="5" height="5" viewBox="0 0 5 5"><path d="M1 0 L4 2.5 L1 5Z" fill="#fff"/></svg></span></div>
  <div class="abs col-rule" style="left:403px;top:846px;width:254px"></div>

  <div class="abs date" style="left:404px;top:857px"><div class="date-box"><div class="date-day narrow">25</div><div class="date-mon">May</div></div><div class="date-year narrow">2014</div></div>
  <p class="abs news-text" style="left:445px;top:857px">Lorem Ipsum is simply dummy text of the printing and typesetting industry. Lorem Ipsum has been the industry's standard dummy text ever since the 1500s,</p>
  <div class="abs date" style="left:404px;top:902px"><div class="date-box"><div class="date-day narrow">25</div><div class="date-mon">May</div></div><div class="date-year narrow">2014</div></div>
  <p class="abs news-text" style="left:445px;top:902px">Lorem Ipsum is simply dummy text of the printing and typesetting industry. Lorem Ipsum has been the industry's standard dummy text ever since the 1500s,</p>
  <div class="abs date" style="left:404px;top:948px"><div class="date-box"><div class="date-day narrow">25</div><div class="date-mon">May</div></div><div class="date-year narrow">2014</div></div>
  <p class="abs news-text" style="left:445px;top:948px">Lorem Ipsum is simply dummy text of the printing and typesetting industry. Lorem Ipsum has been the industry's standard dummy text ever since the 1500s,</p>
</section>

<footer>
  <div class="abs footer"></div>
  <h3 class="abs foot-title" style="left:101px;top:1020px">Quick Link</h3>
  <ul class="abs foot-list" style="left:103px;top:1041px"><li>Home</li><li>Dogs</li><li>Cats</li><li>Our Story</li><li>The Scoop</li><li>Find a Retailer</li><li>Retailers</li></ul>
  <ul class="abs foot-list" style="left:165px;top:1041px"><li>Reservations</li><li>Event Calendar</li><li>Photo galleries</li><li>Video galleries</li></ul>

  <h3 class="abs foot-title" style="left:261px;top:1020px">Contact Us</h3>
  <div class="abs foot-contact" style="left:261px;top:1041px">
    Mossy Den Pet Supply<br>Fernway Road, Harbor Town<br>Phone : <b>+0198 765 432</b><br>Fax : <b>+0198 765 432</b><br>Skype ID: mossyden
  </div>

  <h3 class="abs foot-title" style="left:380px;top:1020px">Recent FB posts,</h3>
  <div class="abs fb-dot" style="left:380px;top:1044px"></div>
  <p class="abs fb-text" style="left:403px;top:1042px">Lorem Ipsum is simply dummy text of the printing and typesetting industry. Lorem Ipsum has been the industry's standard dummy text ever since the 1500s,</p>
  <div class="abs fb-dot" style="left:380px;top:1088px"></div>
  <p class="abs fb-text" style="left:403px;top:1086px">Lorem Ipsum is simply dummy text of the printing and typesetting industry. Lorem Ipsum has been the industry's standard dummy text ever since the 1500s,</p>

  <div class="abs foot-rule"></div>
  <div class="abs follow">Follow us on&nbsp;<i></i><i></i><i></i></div>
  <div class="abs copyright">Copyright © 2014 MossyDenPetSupply.com. All Rights Reserved.<br>Privacy Policy &nbsp;|&nbsp; Terms &amp; Conditions</div>
</footer>

</body>
</html>
```